Dornick and Associates Business Card

A business card that can be templates for all employees using our newly created logo and information. We are looking for stylish however simplistic in nature, clean looks are better than over the top, however creativity will be appreciated if it has the right appeal. Note: If you feel a type of card (plastic, metalic, carbon, raised lettering, etc) helps your design please specify.
Target Market(s)
Investigation ETC
Industry/Entity Type
Private Investigator
Contact Information for Business Card
Len Dornick
President
5173 Wexbury Road
Hermitage PA 16390-4412
Cell: 724-555-0193; Office: 724-555-0147
Email: lendornick@dornickassociates.example
Font styles to use
Requirements
Must have
- Website DornickAssociates.example
- Name, address, phone number ETC
- Use of current Logo and color pallets if applicable
- TM By logo, small

Nice to have
- Would like to see with and without a photo on the design

Should not have
- Redesign of logo, changing of colors

```html
<!DOCTYPE html>
<html lang="en">
<head>
<meta charset="utf-8">
<title>Dornick and Associates Business Card</title>
<link rel="stylesheet" href="https://fonts.googleapis.com/css2?family=Tinos:wght@400;700&family=Arimo:wght@400&display=swap">
<style>
  :root {
    --navy: #27266a;
    --black: #0b0b0b;
    --paper: #f1f1f1;
    --white: #ffffff;
    --backdrop: #e4e4e2;
  }
  html, body {
    margin: 0;
    width: 1200px;
    height: 800px;
    overflow: hidden;
    background: var(--backdrop);
  }
  .canvas {
    width: 1200px;
    height: 800px;
    display: flex;
    align-items: center;
    justify-content: center;
    gap: 40px;
  }
  .card {
    width: 525px;
    height: 300px;
    display: block;
    box-shadow: 0 6px 18px rgba(0,0,0,0.18);
  }
  .firm-name {
    font-family: "Tinos", "Times New Roman", serif;
    font-weight: 700;
  }
  .firm-name--front { fill: var(--black); font-size: 24px; }
  .firm-name--back { fill: var(--navy); font-size: 27px; }
  .person-name {
    font-family: "Tinos", "Times New Roman", serif;
    fill: var(--white);
    font-size: 14px;
  }
  .person-title, .contact-line {
    font-family: "Arimo", Arial, sans-serif;
    fill: var(--white);
  }
  .person-title { font-size: 10.5px; }
  .contact-line { font-size: 8.6px; }
</style>
</head>
<body>
<main class="canvas">

  <svg class="card card--front" viewBox="0 0 350 200" aria-label="Business card front">
    <rect class="card-paper" width="350" height="200" fill="var(--paper)"/>
    <path class="navy-wave" d="M0,134 C130,152 280,125 350,52 L350,200 L0,200 Z" fill="var(--navy)"/>
    <path class="black-swoosh" d="M30,134 C150,150 270,126 330,62 C285,128 160,158 30,134 Z" fill="var(--black)"/>
    <text class="firm-name firm-name--front" x="168" y="80" text-anchor="middle">Dornick and Associates</text>

    <text class="person-name" x="22" y="176">Len Dornick</text>
    <text class="person-title" x="22" y="188">President</text>

    <line class="contact-divider" x1="108" y1="150" x2="108" y2="192" stroke="var(--white)" stroke-width="0.8"/>

    <g class="icon icon--phone" transform="translate(116,154)">
      <rect width="8" height="8" rx="1" fill="var(--white)"/>
      <path d="M2,3 h4 v3 h-4 z" fill="var(--navy)"/>
    </g>
    <text class="contact-line" x="128" y="161">555-555-0193</text>

    <g class="icon icon--mobile" transform="translate(116,166)">
      <rect width="8" height="8" rx="1" fill="var(--white)"/>
      <rect x="2.5" y="1.5" width="3" height="5" fill="var(--navy)"/>
    </g>
    <text class="contact-line" x="128" y="173">555-555-0147</text>

    <g class="icon icon--pin" transform="translate(116,178)">
      <rect width="8" height="8" rx="1" fill="var(--white)"/>
      <circle cx="4" cy="3.6" r="1.8" fill="var(--navy)"/>
      <path d="M2.6,4.6 L4,7 L5.4,4.6 Z" fill="var(--navy)"/>
    </g>
    <text class="contact-line" x="128" y="185">5173 Wexbury Road, Larkfield QX 16390-4412</text>
  </svg>

  <svg class="card card--back" viewBox="0 0 350 200" aria-label="Business card back">
    <rect class="band band--top" width="350" height="200" fill="var(--black)"/>
    <rect class="band band--middle" y="74" width="350" height="58" fill="var(--paper)"/>
    <line class="rule rule--top" x1="0" y1="69" x2="350" y2="69" stroke="var(--paper)" stroke-width="0.8"/>
    <line class="rule rule--bottom" x1="0" y1="137" x2="350" y2="137" stroke="var(--paper)" stroke-width="0.8"/>
    <text class="firm-name firm-name--back" x="175" y="112" text-anchor="middle">Dornick and Associates</text>
  </svg>

</main>
</body>
</html>
```